Adult dating site banners and payment page concepts

We need an overhaul done on our banners, as well as rebranding our packages. We have uploaded a full description of what we need doing, we are not looking for you do do all of them right now. We are looking for a concept for one site banner, one version of the payment page, and one affiliate banner. We will then pay the winner to do the rest of the design work we need to get them all done, but we have uploaded all the bits we will eventually need.

Colors

Designer to choose colors to be used in the design.

Requirements
Must have
• Banner design brief
• We are looking for a new design for all of our upgrade banners for our adult dating swingers sites as well as our payment pages so they need to appeal to men, women, and couples. We are looking for something fun and sexy that really looks nice on mobile and desktop.
• Important design notes banners
• 1. Where you see the word “Extras” we are changing it to a package called “Plus, this can be the word Plus or the + symbol, or both”, we are looking for a design for this.
• 2. Where you see the word “Premium” we are now calling it “Supporter” so that needs some nice font or design as well.
• 3. We would like the offers to jump out at you with the discounts etc.
• 4. The banners need to be able to work on our different sites on the following colours:
• South Africa #7e0202
• UK #0d72ba
• Canada #147eab
• Ireland #003a15
• Australia #272f47
• New Zealand #446160
• Payment pages
• 1. We would like to keep them clean as most of our users are on mobile
• 2. But if you think they can be improved to help with conversion rates we would like to see it.
• Affiliate banners
• We also advertise our sites on other websites using geo-targeted banners; we need to tempt people to click through. The ones we have right now are not animated and we like the idea of that, something saucy and sexy but not porn related. We would like these to be re designed to be something sexier that grabs your attention.

```html
<!DOCTYPE html>
<html lang="en">
<head>
<meta charset="utf-8">
<title>Upgrade Now – Payment Plan</title>
<link rel="stylesheet" href="https://fonts.googleapis.com/css2?family=PT+Sans:wght@400;700&display=swap">
<style>
  :root {
    --orange: #ef9c3c;
    --orange-light: #f5a62a;
    --orange-deep: #e3901a;
    --orange-dark: #d4812a;
    --red: #fb003e;
    --tick: #e8193f;
    --ink: #111111;
    --white: #ffffff;
    --rule: #bdbdbd;
  }
  * { margin: 0; padding: 0; box-sizing: border-box; }
  html, body { width: 1200px; height: 2613px; overflow: hidden; background: var(--white); }
  body { font-family: "PT Sans", sans-serif; color: var(--ink); }
  .page {
    position: relative; width: 1200px; height: 2613px; overflow: hidden;
    border: 3px solid var(--orange); background: var(--white);
  }
  .hero { position: absolute; left: 0; top: 0; width: 1200px; height: 500px; }
  .hero svg { position: absolute; left: 0; top: 0; }
  .hero-title {
    position: absolute; left: 0; width: 100%; top: 78px; text-align: center;
    color: var(--white); font-size: 112px; letter-spacing: 2px; line-height: 1;
  }
  .hero-rule { position: absolute; left: 209px; width: 771px; top: 228px; height: 3px; background: var(--white); }
  .hero-subtitle {
    position: absolute; left: 0; width: 100%; top: 318px; text-align: center;
    color: var(--white); font-size: 76px; line-height: 1;
  }
  .toggle, .actions {
    position: absolute; left: 171px; width: 858px; height: 146px;
    border-radius: 73px; overflow: hidden; display: flex;
  }
  .toggle { top: 540px; }
  .actions { top: 2428px; }
  .toggle span, .actions span {
    flex: 1; display: flex; align-items: center; justify-content: center; font-size: 64px;
  }
  .actions span { font-size: 50px; }
  .is-supporter { background: var(--red); color: var(--white); }
  .is-plus { background: var(--orange); color: var(--ink); }
  .plan-card {
    position: absolute; top: 749px; width: 490px; height: 265px; border-radius: 13px;
    text-align: center;
  }
  .plan-card.is-supporter { left: 71px; }
  .plan-card.is-plus { left: 636px; }
  .plan-name { position: absolute; top: 26px; width: 100%; font-size: 43px; }
  .plan-price { position: absolute; top: 80px; width: 100%; font-size: 92px; font-weight: 700; letter-spacing: 3px; line-height: 1.1; }
  .plan-period { position: absolute; top: 192px; width: 100%; font-size: 31px; }
  .features { position: absolute; left: 0; top: 1041px; width: 1200px; }
  .feature { position: relative; height: 145.5px; }
  .feature::after {
    content: ""; position: absolute; left: 176px; width: 853px; bottom: 0; height: 3px; background: var(--rule);
  }
  .feature:last-child::after { display: none; }
  .feature-name {
    position: absolute; left: 176px; width: 853px; top: 0; height: 145.5px;
    display: flex; align-items: center; justify-content: center; font-size: 46px; letter-spacing: 1px;
  }
  .mark {
    position: absolute; top: 0; height: 145.5px; width: 100px;
    display: flex; align-items: center; justify-content: center; font-size: 46px;
  }
  .mark.left { left: 49px; }
  .mark.right { left: 1047px; }
  .tick { width: 62px; height: 70px; }
</style>
</head>
<body>
<svg width="0" height="0" style="position:absolute">
  <defs>
    <symbol id="tick" viewBox="0 0 62 70">
      <path d="M2 42 L10 36 L20 54 C30 32 44 14 60 2 C46 20 32 42 22 68 L18 68 Z" fill="var(--tick)"/>
    </symbol>
  </defs>
</svg>
<main class="page">
  <header class="hero">
    <svg width="1200" height="500" viewBox="0 0 1200 500">
      <defs><clipPath id="disc"><circle cx="600" cy="-210" r="708"/></clipPath></defs>
      <g clip-path="url(#disc)">
        <rect x="0" y="-300" width="1200" height="800" fill="var(--orange-light)"/>
        <circle cx="240" cy="140" r="200" fill="var(--orange)" opacity="0"/>
        <ellipse cx="420" cy="-60" rx="900" ry="400" fill="var(--orange)"/>
        <ellipse cx="560" cy="-250" rx="900" ry="590" fill="var(--orange-light)"/>
        <circle cx="1200" cy="-100" r="690" fill="var(--orange-dark)"/>
        <circle cx="1080" cy="-260" r="700" fill="var(--orange-deep)"/>
      </g>
    </svg>
    <h1 class="hero-title">UPGRADE NOW</h1>
    <div class="hero-rule"></div>
    <p class="hero-subtitle">Payment Plan</p>
  </header>

  <nav class="toggle">
    <span class="is-supporter">Monthly</span>
    <span class="is-plus">Yearly</span>
  </nav>

  <section class="plan-card is-supporter">
    <div class="plan-name">Supporter</div>
    <div class="plan-price">R134,95</div>
    <div class="plan-period">Monthly</div>
  </section>
  <section class="plan-card is-plus">
    <div class="plan-name">Plus +</div>
    <div class="plan-price">R154,95</div>
    <div class="plan-period">Monthly</div>
  </section>

  <ul class="features">
    <li class="feature"><span class="mark left"><svg class="tick"><use href="#tick"/></svg></span><span class="feature-name">Cancel at any time</span><span class="mark right"><svg class="tick"><use href="#tick"/></svg></span></li>
    <li class="feature"><span class="mark left"><svg class="tick"><use href="#tick"/></svg></span><span class="feature-name">Unlimited Messaging</span><span class="mark right"><svg class="tick"><use href="#tick"/></svg></span></li>
    <li class="feature"><span class="mark left"><svg class="tick"><use href="#tick"/></svg></span><span class="feature-name">Adult Photos and Videos</span><span class="mark right"><svg class="tick"><use href="#tick"/></svg></span></li>
    <li class="feature"><span class="mark left"><svg class="tick"><use href="#tick"/></svg></span><span class="feature-name">Full Chatroom Access</span><span class="mark right"><svg class="tick"><use href="#tick"/></svg></span></li>
    <li class="feature"><span class="mark left"><svg class="tick"><use href="#tick"/></svg></span><span class="feature-name">Send Statuses to Friends &amp; Followers</span><span class="mark right"><svg class="tick"><use href="#tick"/></svg></span></li>
    <li class="feature"><span class="mark left">2</span><span class="feature-name">Chatroom Webcams</span><span class="mark right">7</span></li>
    <li class="feature"><span class="mark left">-</span><span class="feature-name">Send Statuses to Matches</span><span class="mark right"><svg class="tick"><use href="#tick"/></svg></span></li>
    <li class="feature"><span class="mark left">-</span><span class="feature-name">Multiple Chat Access for Couples</span><span class="mark right"><svg class="tick"><use href="#tick"/></svg></span></li>
    <li class="feature"><span class="mark left">-</span><span class="feature-name">HD Photos and Videos</span><span class="mark right"><svg class="tick"><use href="#tick"/></svg></span></li>
  </ul>

  <div class="actions">
    <span class="is-supporter">Upgrade Now</span>
    <span class="is-plus">Upgrade Now</span>
  </div>
</main>
</body>
</html>
```